TEAL BEACON LICE REMOVAL labels

I need a label design for our MINT REPELLING SHAMPOO (LICE PREVENTION).
It also includes our MINT REPELLING CONDITIONER (LICE PREVENTION) and our MINT SPRAY (LICE PREVENTION) also includes LICE & NIT ELIMINATING MOUSSE (LICE TREATMENT) and a LICE ELIMINATOR 100% Dimethicone oil (LICE TREATMENT). The shampoo and conditioner are sulfate free, contains peppermint and other essential oils and is safe for the entire family. Label should be simple, modern and high end looking. Fun is good too if it looks nice!

Target Market(s)

Kids and Adults

Industry/Entity Type

Hair Care Product

Font styles to use
Sans Serif
Decorative

Requirements
Must have
• -Words that should be used: safe, non toxic, sulfate free, essential oils, pesticide free. - Naturally removes lice, super lice & nits are great words for the lice & nit eliminating mousse and treatment oil 100% Dimethicone oil
- On a side note there are no essential oils in the lice & nit eliminating mousse or treatment oil 100% Dimethicone oil
Nice to have
• Earth tone colors if possible
Kid safe, no fillers, colors or scents
100% effective (even against super lice)
8oz labels and 4oz labels
Should not have
• No pictures of lice

```html
<!DOCTYPE html>
<html lang="en">
<head>
<meta charset="utf-8">
<title>Teal Beacon Lice Removal — Mint Repelling Labels</title>
<link href="https://fonts.googleapis.com/css2?family=Montserrat:wght@500;600;700&display=swap" rel="stylesheet">
<style>
  :root {
    --page-bg: #f4f6f4;
    --ink-green: #1f6b3a;
    --ink-white: #ffffff;
    --shampoo-light: #a9cfc4;
    --shampoo-mid: #7fb6a4;
    --shampoo-lilac: #a8b8cf;
    --conditioner-light: #6fa682;
    --conditioner-mid: #4f8c66;
    --conditioner-deep: #3c7b57;
    --brand-disc: #ffffff;
  }
  * { box-sizing: border-box; margin: 0; padding: 0; }
  html, body { width: 1200px; height: 1000px; overflow: hidden; }
  body {
    background: var(--page-bg);
    font-family: "Montserrat", sans-serif;
  }
  .canvas {
    position: relative;
    width: 1200px;
    height: 1000px;
    display: flex;
    justify-content: center;
    align-items: center;
    gap: 60px;
  }
  .label {
    position: relative;
    width: 320px;
    height: 640px;
    overflow: hidden;
    border-radius: 4px;
    box-shadow: 0 6px 24px rgba(20, 60, 40, 0.15);
  }
  .label-art {
    position: absolute;
    inset: 0;
  }
  .label--shampoo .label-art {
    background:
      radial-gradient(ellipse at 30% 80%, var(--shampoo-lilac) 0%, transparent 55%),
      linear-gradient(165deg, var(--shampoo-light) 0%, var(--shampoo-mid) 55%, var(--shampoo-light) 100%);
  }
  .label--conditioner .label-art {
    background:
      radial-gradient(ellipse at 70% 30%, var(--conditioner-light) 0%, transparent 60%),
      linear-gradient(165deg, var(--conditioner-mid) 0%, var(--conditioner-deep) 60%, var(--conditioner-mid) 100%);
  }
  .brand {
    position: absolute;
    top: 60px;
    left: 0;
    right: 0;
    display: flex;
    flex-direction: column;
    align-items: center;
    gap: 10px;
  }
  .brand-disc {
    width: 72px;
    height: 72px;
    border-radius: 50%;
    background: var(--brand-disc);
  }
  .brand-name {
    font-weight: 600;
    font-size: 11px;
    letter-spacing: 2px;
    text-align: center;
    color: var(--ink-white);
  }
  .product-name {
    position: absolute;
    top: 310px;
    left: 26px;
    font-weight: 600;
    font-size: 25px;
    line-height: 1.25;
    letter-spacing: 0.5px;
  }
  .label--shampoo .product-name { color: var(--ink-green); }
  .label--conditioner .product-name { color: var(--ink-white); }
  .claims {
    position: absolute;
    left: 18px;
    right: 14px;
    bottom: 30px;
    color: var(--ink-white);
    font-weight: 500;
    font-size: 8.5px;
    line-height: 1.35;
  }
  .claims-tags {
    margin-top: 10px;
    font-weight: 700;
    font-size: 8.5px;
  }
</style>
</head>
<body>
<main class="canvas">
  <section class="label label--shampoo">
    <div class="label-art" role="img" aria-label="Soft mint and lilac watercolour wash with a faint line drawing of mint leaves"></div>
    <div class="brand">
      <span class="brand-disc"></span>
      <span class="brand-name">TEAL BEACON<br>LICE REMOVAL</span>
    </div>
    <h2 class="product-name">MINT REPELLING<br>SHAMPOO</h2>
    <div class="claims">
      <p>Naturally removes lice<br>super lice &amp; nits are great words for the lice<br>&amp; nit eliminating mousse and treatment oil %100 Dim</p>
      <p class="claims-tags">safe | non toxic | sulfate free | essential oils | pesticide free</p>
    </div>
  </section>

  <section class="label label--conditioner">
    <div class="label-art" role="img" aria-label="Deep green watercolour wash with a faint line drawing of mint leaves"></div>
    <div class="brand">
      <span class="brand-disc"></span>
      <span class="brand-name">TEAL BEACON<br>LICE REMOVAL</span>
    </div>
    <h2 class="product-name">MINT REPELLING<br>CONDITIONER</h2>
    <div class="claims">
      <p>Naturally removes lice<br>super lice &amp; nits are great words for the lice<br>&amp; nit eliminating mousse and treatment oil %100 Dim</p>
      <p class="claims-tags">safe | non toxic | sulfate free | essential oils | pesticide free</p>
    </div>
  </section>
</main>
</body>
</html>
```